jpg 'poster' for music show to use on social media (only 72dpi needed)

style wanted: Milo Grent goes western

text:

Ray Dunkel
Anna Prescot
Neil Tomasek
Maribeth Oskarsen
... and friends

Friday April 25
Tinbarrel Coffee
Seattle

7:00 PM

$5

would love to get ASAP.

committed to pay for a cool poster!
just need 72 dpi. Thx!

not crazy particular. a cool Milo Grent type layout will be accepted :)

```html
<!DOCTYPE html>
<html lang="en">
<head>
<meta charset="utf-8">
<title>Ray Dunkel and Friends — Friday April 25 — Tinbarrel Coffee</title>
<link rel="stylesheet" href="https://fonts.googleapis.com/css2?family=Delius+Unicase:wght@700&display=swap">
<style>
  :root {
    --poster-red: #ff2a00;
    --band-black: #000000;
    --type-white: #ffffff;
  }
  html, body {
    margin: 0;
    padding: 0;
    width: 930px;
    height: 1200px;
    overflow: hidden;
    background: var(--poster-red);
  }
  .poster {
    display: block;
    width: 930px;
    height: 1200px;
  }
  .poster__field { fill: var(--poster-red); }
  .poster__frame {
    fill: none;
    stroke: var(--band-black);
    stroke-width: 4;
    stroke-linejoin: miter;
  }
  .band { fill: var(--band-black); }
  .band-text {
    fill: var(--type-white);
    font-family: "Delius Unicase", "Comic Sans MS", sans-serif;
    font-weight: 700;
    text-transform: uppercase;
  }
</style>
</head>
<body>
<svg class="poster" viewBox="0 0 930 1200" xmlns="http://www.w3.org/2000/svg" role="img" aria-label="Ray Dunkel, Maribeth Oskarsen, Anna Prescot, Neil Tomasek and friends. Friday April 25, 7 PM, $5, Tinbarrel Coffee, Seattle">
  <rect class="poster__field" x="0" y="0" width="930" height="1200"/>

  <!-- hand-drawn frame -->
  <g class="poster-frame">
    <polygon class="poster__frame" points="30,14 880,10 888,1170 44,1180"/>
    <polygon class="poster__frame" points="36,22 872,18 880,1162 50,1172"/>
  </g>

  <!-- headliner -->
  <g class="lineup-band lineup-band--headliner">
    <polygon class="band" points="92,58 832,52 826,168 96,172"/>
    <text class="band-text" x="462" y="153" font-size="118" text-anchor="middle" textLength="700" lengthAdjust="spacingAndGlyphs">Ray Dunkel</text>
  </g>

  <g class="lineup-band">
    <polygon class="band" points="28,196 898,194 894,288 30,292"/>
    <text class="band-text" x="462" y="272" font-size="76" text-anchor="middle" textLength="850" lengthAdjust="spacingAndGlyphs">Maribeth Oskarsen</text>
  </g>

  <g class="lineup-band">
    <polygon class="band" points="62,312 884,308 888,402 60,404"/>
    <text class="band-text" x="472" y="392" font-size="82" text-anchor="middle" textLength="800" lengthAdjust="spacingAndGlyphs">Anna Prescot</text>
  </g>

  <g class="lineup-band">
    <polygon class="band" points="34,418 884,420 880,546 36,544"/>
    <text class="band-text" x="458" y="522" font-size="104" text-anchor="middle" textLength="830" lengthAdjust="spacingAndGlyphs">Neil Tomasek</text>
  </g>

  <g class="lineup-band lineup-band--friends">
    <polygon class="band" points="104,588 856,582 852,688 108,692"/>
    <text class="band-text" x="480" y="670" font-size="78" text-anchor="middle" textLength="700" lengthAdjust="spacingAndGlyphs">...and friends</text>
  </g>

  <!-- date and details -->
  <g class="detail-band detail-band--date">
    <polygon class="band" points="62,744 896,740 898,830 60,834"/>
    <text class="band-text" x="478" y="816" font-size="76" text-anchor="middle" textLength="810" lengthAdjust="spacingAndGlyphs">Friday&#160;&#160;April 25</text>
  </g>

  <g class="detail-band detail-band--time">
    <polygon class="band" points="94,852 448,850 446,958 98,962"/>
    <text class="band-text" x="264" y="940" font-size="82" text-anchor="middle" textLength="270" lengthAdjust="spacingAndGlyphs">7 PM</text>
  </g>

  <g class="detail-band detail-band--price">
    <polygon class="band" points="544,846 868,848 866,948 542,946"/>
    <text class="band-text" x="706" y="922" font-size="82" text-anchor="middle" textLength="130" lengthAdjust="spacingAndGlyphs">$5</text>
  </g>

  <g class="detail-band detail-band--venue">
    <polygon class="band" points="92,972 912,968 914,1122 90,1126"/>
    <text class="band-text" x="506" y="1046" font-size="76" text-anchor="middle" textLength="820" lengthAdjust="spacingAndGlyphs">Tinbarrel Coffee</text>
    <text class="band-text" x="484" y="1110" font-size="72" text-anchor="middle" textLength="380" lengthAdjust="spacingAndGlyphs">Seattle</text>
  </g>
</svg>
</body>
</html>
```